New Bicycle shop business card

Hi!
I'm looking for a business card for my new proffesional bike mechanics shop. This shop is only for fixing broken bikes and not selling bikes.
Peferbly a modern and sleek and modern design.
Colors: black, grey, red, white
Information:
Name: Rijwielwerkplaats Vanhoutem
Shop owner: Bart Vanhoutem & Sanne Maertens
Website: www.rijwielwerkplaats-vanhoutem.be
Email: info@rijwielwerkplaats-vanhoutem.be
Phone number: +32471902386
Street adres: Kerkweg 64
9970 Oostmoere
Slogan/shop information: Herstellingen van alle merken.
Logo: see files.
Target Market(s)
People who seek a mechanic to fix or upgrade their bikes.
Contact Information for Business Card
Information:
Website: info@rijwielwerkplaats-vanhoutem.be
9970 Oostmoere
Logo: see files.

```html
<!DOCTYPE html>
<html lang="nl">
<head>
<meta charset="utf-8">
<title>Rijwielwerkplaats Vanhoutem – visitekaartje</title>
<link href="https://fonts.googleapis.com/css2?family=Montserrat:wght@500;600;700;800&display=swap" rel="stylesheet">
<style>
  :root {
    --stage: #2c2e31;
    --card-black: #141416;
    --card-black-soft: #1e1f22;
    --red: #e0203c;
    --white: #ffffff;
    --ink: #141416;
    --grey: #8a8c90;
  }
  * { box-sizing: border-box; margin: 0; padding: 0; }
  html, body { width: 1200px; height: 1200px; overflow: hidden; }
  body {
    background: var(--stage);
    font-family: "Montserrat", sans-serif;
    position: relative;
  }
  .card {
    position: absolute;
    left: 150px;
    width: 900px;
    height: 514px;
    border-radius: 4px;
    overflow: hidden;
    box-shadow: 0 18px 40px rgba(0,0,0,.45);
  }
  .card--front { top: 60px; }
  .card--back  { top: 626px; }

  .card-surface {
    position: absolute; inset: 0;
    background: radial-gradient(circle at 40% 35%, var(--card-black-soft), var(--card-black) 75%);
  }

  /* front */
  .front-content {
    position: absolute; inset: 0;
    display: flex; flex-direction: column; align-items: center; justify-content: center;
    gap: 26px;
  }
  .brand { display: flex; align-items: center; gap: 24px; }
  .brand-dot { width: 70px; height: 70px; border-radius: 50%; background: var(--red); flex: none; }
  .brand-name {
    color: var(--white); font-weight: 800; text-transform: uppercase;
    font-size: 40px; line-height: 1.1; letter-spacing: 1px;
  }
  .slogan {
    color: var(--white); font-weight: 500; text-transform: uppercase;
    font-size: 24px; letter-spacing: 6px;
  }

  /* back */
  .back-brand {
    position: absolute; left: 40px; top: 70px;
    display: flex; flex-direction: column; gap: 16px;
  }
  .back-brand .brand-dot { width: 48px; height: 48px; }
  .back-brand .brand-name { font-size: 24px; }

  .contact-panel {
    position: absolute; left: 400px; top: 0; right: 0; bottom: 0;
    background: var(--white);
    padding: 48px 30px 0 56px;
  }
  .owners { font-size: 25px; font-weight: 700; color: var(--ink); }
  .role { font-size: 20px; font-weight: 600; color: var(--red); margin-top: 4px; }
  .contact-list { list-style: none; margin-top: 34px; }
  .contact-item {
    position: relative; height: 76px;
    display: flex; flex-direction: column; justify-content: center;
    font-size: 20px; font-weight: 700; color: var(--ink); line-height: 1.3;
  }
  .contact-icon {
    position: absolute; left: -86px; top: 50%;
    width: 60px; height: 60px; margin-top: -30px;
    border-radius: 50%; background: var(--white);
    display: flex; align-items: center; justify-content: center;
  }
  .contact-icon svg { width: 26px; height: 26px; }
</style>
</head>
<body>

<section class="card card--front" aria-label="Voorkant visitekaartje">
  <div class="card-surface" role="img" aria-label="Zwart oppervlak met fijn stippenpatroon"></div>
  <div class="front-content">
    <div class="brand">
      <span class="brand-dot"></span>
      <p class="brand-name">Rijwielwerkplaats<br>Vanhoutem</p>
    </div>
    <p class="slogan">Herstellingen van alle merken</p>
  </div>
</section>

<section class="card card--back" aria-label="Achterkant visitekaartje">
  <div class="card-surface" role="img" aria-label="Zwart oppervlak met fijn stippenpatroon"></div>
  <div class="back-brand">
    <span class="brand-dot"></span>
    <p class="brand-name">Rijwielwerkplaats<br>Vanhoutem</p>
  </div>

  <div class="contact-panel">
    <p class="owners">Bart Vanhoutem &amp; Sanne Maertens</p>
    <p class="role">Shop owner</p>
    <ul class="contact-list">
      <li class="contact-item">
        <span class="contact-icon">
          <svg viewBox="0 0 24 24"><path d="M12 3 2 12h3v9h5v-6h4v6h5v-9h3z" fill="var(--red)"/></svg>
        </span>
        <span>Kerkweg 64</span><span>9970 Oostmoere</span>
      </li>
      <li class="contact-item">
        <span class="contact-icon">
          <svg viewBox="0 0 24 24"><rect x="6" y="2" width="12" height="20" rx="2" fill="none" stroke="var(--red)" stroke-width="2"/><circle cx="12" cy="18" r="1.3" fill="var(--red)"/></svg>
        </span>
        <span>+32471902386</span>
      </li>
      <li class="contact-item">
        <span class="contact-icon">
          <svg viewBox="0 0 24 24"><circle cx="12" cy="12" r="9" fill="none" stroke="var(--red)" stroke-width="2"/><path d="M3 12h18M12 3c3 3 3 15 0 18M12 3c-3 3-3 15 0 18" fill="none" stroke="var(--red)" stroke-width="1.6"/></svg>
        </span>
        <span>www.rijwielwerkplaats-vanhoutem.be</span>
      </li>
      <li class="contact-item">
        <span class="contact-icon">
          <svg viewBox="0 0 24 24"><rect x="2" y="5" width="20" height="14" rx="1" fill="var(--red)"/><path d="M2 6l10 7 10-7" fill="none" stroke="var(--white)" stroke-width="1.8"/></svg>
        </span>
        <span>info@rijwielwerkplaats-vanhoutem.be</span>
      </li>
    </ul>
  </div>
</section>

</body>
</html>
```